Kettle Ledger Business Card design

We need a stand out business card design for Accounting practice based in Australia specialising in pubs, clubs and hotels. We help venues maximise margins, create time and manage cashflow. One club we have been working with for the last 6 months has increased revenue by 3% and margin by 5% in this time frame. We have a back office outsourced system that costs less than having a full time employee and also allows the venues the added benefit of:<br/>-using the office space to become a revenue generating opportunity. <br/>-a complete system to enhance governance, accountability and efficiency within their operation<br/>-52 weeks cover so no hassle to cover annual/sick .. leave<br/><br/>We would like to see designs that use the colours of our logo (green & blue).
Target Market(s)
Australian Pubs, Clubs & Hotels abookkeeping, accounting and tax services
Industry/Entity Type
Accountant
Contact Information for Business Card
Miriam Oakley CPA
Principal
Accountant Tax Agent
Miriam@KettleLedger-example.com.au
0418693142
www.kettleledger-example.com.au
Accounting / Payroll / Tax / SMSF / Technology
Colors
Designer to choose colors to be used in the design.
Look and feel
Each slider illustrates characteristics of the customer's brand and the style your logo design should communicate.

```html
<!DOCTYPE html>
<html lang="en">
<head>
<meta charset="utf-8">
<title>Kettle Ledger Business Card</title>
<link rel="stylesheet" href="https://fonts.googleapis.com/css2?family=Montserrat:wght@700;800&family=Lato:wght@400;700&display=swap">
<style>
  :root {
    --brand-blue: #24409a;
    --brand-blue-soft: #2d4ba6;
    --brand-green: #117341;
    --paper: #ffffff;
    --backdrop: #e6e7ea;
    --card-shadow: 0 10px 28px rgba(20, 30, 60, 0.22);
  }
  * { box-sizing: border-box; margin: 0; padding: 0; }
  html, body {
    width: 1200px; height: 900px; overflow: hidden;
    background: var(--backdrop);
    font-family: "Lato", Arial, sans-serif;
  }
  .stage { position: relative; width: 1200px; height: 900px; }
  .card {
    position: absolute; left: 250px; width: 700px; height: 400px;
    border-radius: 18px; overflow: hidden; box-shadow: var(--card-shadow);
  }
  /* Back side */
  .card-back { top: 35px; background: var(--brand-blue); }
  .back-pattern {
    position: absolute; inset: 0;
    background: linear-gradient(135deg, var(--brand-blue) 0%, var(--brand-blue-soft) 100%);
  }
  .back-brand { position: absolute; left: 400px; top: 120px; color: var(--paper); }
  .back-brand .firm-name {
    font-family: "Montserrat", Arial, sans-serif; font-weight: 800;
    font-size: 34px; line-height: 1; letter-spacing: -0.5px;
  }
  .service-stack {
    list-style: none; margin-top: 10px; padding-left: 4px;
    font-family: "Montserrat", Arial, sans-serif; font-weight: 700;
    font-size: 13px; letter-spacing: 1.5px; line-height: 1.35;
  }
  /* Front side */
  .card-front { top: 465px; background: var(--paper); }
  .wave { position: absolute; inset: 0; }
  .wave .wave-blue { fill: var(--brand-blue); }
  .wave .wave-green { fill: var(--brand-green); }
  .front-brand {
    position: absolute; left: 40px; top: 122px;
    display: flex; align-items: center; gap: 12px;
  }
  .brand-dot { width: 20px; height: 20px; border-radius: 50%; background: var(--brand-blue); }
  .front-brand .firm-name {
    font-family: "Montserrat", Arial, sans-serif; font-weight: 800;
    font-size: 40px; color: var(--brand-blue); letter-spacing: -1px; line-height: 1;
  }
  .person { position: absolute; right: 40px; top: 38px; text-align: right; }
  .person-name {
    font-family: "Montserrat", Arial, sans-serif; font-weight: 800;
    font-size: 28px; color: var(--brand-blue); letter-spacing: -0.5px; line-height: 1.2;
  }
  .person-role { font-size: 16px; color: var(--brand-green); line-height: 1.3; margin-top: 4px; }
  .contact-list {
    position: absolute; right: 28px; top: 226px; list-style: none;
    color: var(--paper); font-size: 15px; text-align: right;
  }
  .contact-list li {
    display: flex; align-items: center; justify-content: flex-end; gap: 10px; height: 27px;
  }
  .contact-list svg { width: 16px; height: 16px; fill: none; stroke: var(--paper); stroke-width: 1.8; }
  .service-line {
    position: absolute; left: 36px; bottom: 22px;
    color: var(--paper); font-size: 15px; letter-spacing: 0.3px;
  }
  .service-line .sep { margin: 0 8px; opacity: 0.9; }
</style>
</head>
<body>
<main class="stage">

  <section class="card card-back" aria-label="Business card back">
    <div class="back-pattern" role="img" aria-label="Repeating outline pattern of hop cones in light blue"></div>
    <div class="back-brand">
      <p class="firm-name">Kettle Ledger</p>
      <ul class="service-stack">
        <li>ACCOUNTING</li>
        <li>PAYROLL</li>
        <li>TAX</li>
        <li>SMSF</li>
        <li>TECHNOLOGY</li>
      </ul>
    </div>
  </section>

  <section class="card card-front" aria-label="Business card front">
    <svg class="wave" viewBox="0 0 700 400" preserveAspectRatio="none" aria-hidden="true">
      <path class="wave-green" d="M0,300 C180,300 300,285 380,230 C460,175 540,150 640,145 C540,160 460,190 385,245 C300,305 180,316 0,316 Z"/>
      <path class="wave-blue" d="M0,400 L0,330 C180,328 310,310 395,255 C480,198 560,168 700,160 L700,400 Z"/>
    </svg>

    <div class="front-brand">
      <span class="brand-dot" aria-hidden="true"></span>
      <p class="firm-name">Kettle Ledger</p>
    </div>

    <div class="person">
      <p class="person-name">Miriam Oakley CPA</p>
      <p class="person-role">Principal<br>Accountant Tax Agent</p>
    </div>

    <ul class="contact-list">
      <li>0418693142
        <svg viewBox="0 0 16 16" aria-hidden="true"><path d="M3 2 L6 2 L7 5 L5.5 6.5 C6.5 8.5 7.5 9.5 9.5 10.5 L11 9 L14 10 L14 13 C8 14 2 8 3 2 Z"/></svg>
      </li>
      <li>Miriam@KettleLedger-example.com.au
        <svg viewBox="0 0 16 16" aria-hidden="true"><rect x="1.5" y="3.5" width="13" height="9"/><path d="M1.5 3.5 L8 9 L14.5 3.5"/></svg>
      </li>
      <li>kettleledger-example.com.au
        <svg viewBox="0 0 16 16" aria-hidden="true"><circle cx="8" cy="8" r="6.5"/><path d="M1.5 8 H14.5 M8 1.5 C5 5 5 11 8 14.5 M8 1.5 C11 5 11 11 8 14.5"/></svg>
      </li>
    </ul>

    <p class="service-line">Accounting<span class="sep">|</span>Payroll<span class="sep">|</span>Tax<span class="sep">|</span>SMSF<span class="sep">|</span>Technology</p>
  </section>

</main>
</body>
</html>
```